Website design for a Recruitment Agency in the Pacific Islands

Website for jobseekers to search for work, employers to list vacancies and also for workers to upload their resumes for possible job prospects.

The website will be called ' Korvani Staffing' and this needs to reflect the Pacific Islanders searching for jobs or working in the fields.
Must be connected to a database that collects details for workers which can be downloaded onto an excel spreadsheet for quick reviews offline
The website must also have an app for ios and android so this can be easily downloaded for individuals who want to do quick job searches without going onto the website.

The main objective of this website is to list job opportunities in all Pacific Island Countries or even overseas which Pacific Islanders can apply.

The theme of fishing means ' there is alot of fish in the sea ' = lots of workers in the Pacific Ocean.

Target Market(s)

Agriculture, Fisheries, constructions and mining

Industry/Entity Type

Agriculture, Constructions and Fisheries

Font styles to use
Other font styles liked:
• Muli

Colors
E54698
E96AAD
F1A4CE
F9D9EA
FCEFF6

Requirements
Must have
• Must have an App, adroid and ios
Nice to have
• - pictures of Pacific Islanders , pictures of Pacific Islanders at work in mines, in fisheries and in agricultures

```html
<!DOCTYPE html>
<html lang="en">
<head>
<meta charset="utf-8">
<title>Korvani Staffing — Find the perfect job for you</title>
<link href="https://fonts.googleapis.com/css2?family=Mulish:wght@400;500;600;700;800&display=swap" rel="stylesheet">
<style>
:root{
  --magenta:#e6057f;
  --pink:#e54698;
  --pink-mid:#e96aad;
  --pink-soft:#f1a4ce;
  --pink-pale:#f9d9ea;
  --blush:#fceff6;
  --ink:#111111;
  --text:#333333;
  --muted:#6f6f6f;
  --white:#ffffff;
  --line:#d9d9d9;
}
*{box-sizing:border-box;margin:0;padding:0}
html,body{width:1200px;height:4193px;overflow:hidden}
body{font-family:'Mulish',sans-serif;color:var(--ink);background:var(--white);position:relative}
.abs{position:absolute}
a{color:inherit;text-decoration:none}

/* Hero */
.hero{left:0;top:0;width:1200px;height:727px;background:var(--blush);overflow:hidden}
.hero-shape{left:0;top:0}
.layer-back{left:775px;top:190px;width:300px;height:440px;background:var(--white);border-radius:26px;transform:rotate(8deg)}
.layer-mid{left:745px;top:170px;width:310px;height:445px;background:var(--pink-mid);border-radius:26px;transform:rotate(4deg)}
.hero-photo{left:711px;top:141px;width:315px;height:456px;border-radius:24px;background:linear-gradient(180deg,#aab7c8 0%,#cdd3dc 35%,#c9a86a 62%,#8c7a5c 100%)}
.logo{font-weight:500;font-size:32px;color:var(--ink);letter-spacing:-0.5px;line-height:30px;white-space:nowrap}
.logo span{display:block}
.logo span+span{padding-left:16px}
.nav-logo{left:86px;top:22px}
.nav{left:311px;top:44px;font-size:12.5px;font-weight:500;color:var(--ink)}
.nav a{position:absolute;white-space:nowrap}
.nav .active{color:var(--magenta)}
.nav .light{color:var(--white)}
.upload-btn{left:1008px;top:31px;width:106px;height:44px;border:1.5px solid var(--white);border-radius:22px;color:var(--white);font-size:12.5px;font-weight:600;display:flex;align-items:center;justify-content:center;gap:8px}
.hero-title{left:86px;top:150px;font-size:58px;font-weight:700;line-height:70px;letter-spacing:-0.5px}
.hero-sub{left:86px;top:304px;font-size:15px;color:var(--text)}
.search-bar{left:85px;top:355px;width:459px;height:81px;background:var(--white);border-radius:41px;box-shadow:0 6px 22px rgba(230,5,127,.14);display:flex;align-items:center;padding:0 16px 0 36px;font-size:15px}
.search-bar .divider{width:1px;height:50px;background:var(--line);margin:0 18px 0 58px}
.search-bar .loc{display:flex;align-items:center;gap:6px;flex:1}
.search-bar .chev{margin-left:auto;margin-right:20px}
.find-btn{height:50px;padding:0 22px;border-radius:25px;background:var(--magenta);color:var(--white);font-weight:600;display:flex;align-items:center;font-size:15px}
.popular-title{left:84px;top:473px;font-size:19px;font-weight:600}
.tag{height:38px;padding:0 27px;border-radius:19px;background:var(--white);color:var(--magenta);font-size:14.5px;display:flex;align-items:center}

/* Category */
.section-title{font-size:42px;font-weight:600;letter-spacing:-0.3px}
.cat-title{left:0;width:1200px;top:812px;text-align:center}
.cat-sub{left:0;width:1200px;top:877px;text-align:center;font-size:13px;color:var(--muted)}
.cat-card{width:502px;height:95px;border:1.5px solid #d6d6d6;border-radius:20px;background:var(--white);overflow:hidden;display:flex;align-items:center}
.cat-card.active{background:var(--blush);border-color:var(--blush)}
.cat-icon{width:98px;height:95px;background:var(--blush);display:flex;align-items:center;justify-content:center;flex:none}
.cat-card.active .cat-icon{background:var(--magenta);border-radius:20px}
.cat-text{padding-left:30px}
.cat-text h3{font-size:20px;font-weight:600;margin-bottom:10px}
.cat-text p{font-size:13px;color:var(--text)}
.all-cat{left:0;width:1200px;top:1185px;text-align:center;color:var(--magenta);font-size:15px}

/* Featured */
.featured{left:0;top:1302px;width:1200px;height:1053px;background:var(--blush)}
.feat-title{left:85px;top:1390px}
.feat-sub{left:85px;top:1457px;font-size:13px;color:var(--muted)}
.job-card{width:326px;height:312px;background:var(--white);border-radius:32px}
.job-card .chip{left:40px;top:54px;display:flex;align-items:center;gap:14px;font-size:13.5px;color:var(--text)}
.chip-icon{width:32px;height:32px;border-radius:7px;background:var(--pink-soft);display:flex;align-items:center;justify-content:center}
.job-card h3{position:absolute;left:40px;top:98px;font-size:20px;font-weight:600}
.job-meta{left:40px;top:144px;display:flex;align-items:center;font-size:13px;gap:10px}
.job-meta b{font-weight:700;margin-right:10px}
.job-date{left:40px;top:223px;font-size:12.5px;color:var(--muted);line-height:21px}
.job-date b{color:var(--ink);font-weight:700}
.job-thumb{left:224px;top:210px;width:62px;height:62px;border-radius:13px;background:#0b0b0b}
.all-jobs{left:85px;top:2203px;width:160px;height:51px;border-radius:26px;background:var(--magenta);color:var(--white);font-size:15px;display:flex;align-items:center;justify-content:center;gap:8px}

/* About */
.about-photo{left:0;top:2450px;width:500px;height:545px;background:linear-gradient(135deg,#6a6f63 0%,#a39a86 45%,#c7bca6 70%,#5b5d58 100%);clip-path:polygon(28% 0,100% 50%,62% 100%,0 72%,0 40%)}
.about-ring{left:720px;top:2425px;width:300px;height:300px;border:1.5px solid var(--pink-pale);border-radius:50%}
.about-title{left:557px;top:2560px;font-size:42px;font-weight:600}
.about-copy{left:557px;top:2638px;width:540px;font-size:13.5px;line-height:21px;color:var(--muted)}
.about-copy p+p{margin-top:9px}
.started{left:557px;top:2836px;width:122px;height:44px;border:1.5px solid var(--ink);border-radius:22px;font-size:14px;display:flex;align-items:center;justify-content:center}

/* Contact */
.contact{left:0;top:3093px;width:1200px;height:578px;background:var(--blush)}
.contact-title{left:85px;top:3230px}
.contact-item{left:84px;display:flex;align-items:center;gap:14px;color:var(--magenta);font-weight:700;font-size:15.5px;line-height:19px}
.contact-dot{width:46px;height:46px;border-radius:50%;background:var(--white);display:flex;align-items:center;justify-content:center;flex:none}
.form-card{left:508px;top:3196px;width:606px;height:509px;background:var(--white);border-radius:8px;box-shadow:0 10px 40px rgba(0,0,0,.09)}
.form-card h2{position:absolute;left:55px;top:46px;font-size:42px;font-weight:600}
.field{width:236px}
.field label{display:block;font-size:13.5px;font-weight:700;margin-bottom:12px}
.field span{display:block;font-size:11.5px;color:#9a9a9a;height:24px;border-bottom:1px solid #c9c9c9}
.field.wide{width:492px}
.field.wide span{height:56px}
.caret{width:1px;height:17px;background:var(--ink);display:block}
.submit{left:423px;top:400px;width:122px;height:44px;border-radius:22px;background:var(--magenta);color:var(--white);font-size:15px;display:flex;align-items:center;justify-content:center}

/* Footer */
.foot-logo{left:86px;top:3808px}
.foot-about{left:86px;top:3892px;width:345px;font-size:13px;line-height:21px;color:var(--muted)}
.foot-col h4{font-size:16.5px;font-weight:700}
.foot-col .bar{width:40px;height:3px;background:var(--magenta);margin:14px 0 20px}
.foot-col ul{list-style:none;font-size:12px;color:var(--text)}
.foot-col li{display:flex;align-items:center;gap:10px;height:42px}
.foot-col li::before{content:"»";color:var(--magenta);font-size:13px}
.foot-contact li{display:flex;align-items:flex-start;gap:14px;font-size:11.5px;line-height:15px;height:auto;margin-bottom:20px}
.foot-contact li::before{content:none}
.foot-contact b{font-weight:700}
.foot-rule{top:4128px;height:1px;background:var(--pink-soft)}
.copyright{left:0;width:1200px;top:4119px;text-align:center;font-size:13px;font-weight:700}
</style>
</head>
<body>

<!-- Hero -->
<section class="abs hero">
  <svg class="abs hero-shape" width="1200" height="727" viewBox="0 0 1200 727" aria-hidden="true">
    <path d="M863 0 L652 500 Q630 560 680 600 L800 727 L1200 727 L1200 0 Z" fill="var(--magenta)"/>
  </svg>
  <div class="abs layer-back"></div>
  <div class="abs layer-mid"></div>
  <div class="abs hero-photo" role="img" aria-label="Photo of two workers in hi-vis vests and hard hats on a rocky mining site"></div>

  <div class="abs nav-logo logo"><span>Korvani</span><span>Staffing</span></div>
  <nav class="abs nav">
    <a class="active" style="left:0">Home</a>
    <a style="left:64px">About Us</a>
    <a style="left:146px">Services We Offer Assistance In</a>
    <a style="left:356px">Job Seeker Portal</a>
    <a style="left:482px">Training</a>
    <a class="light" style="left:557px">Info</a>
    <a class="light" style="left:607px">Contact Us</a>
  </nav>
  <a class="abs upload-btn">Upload
    <svg width="14" height="14" viewBox="0 0 14 14" fill="none" stroke="#fff" stroke-width="1.5"><path d="M7 10V2M4 5l3-3 3 3M2 10v2h10v-2"/></svg>
  </a>

  <h1 class="abs hero-title">Find the perfect<br>job for you</h1>
  <p class="abs hero-sub">Search your career opportunity through 12,800 jobs</p>

  <div class="abs search-bar">
    <span>Job Title</span>
    <span class="divider"></span>
    <span class="loc">
      <svg width="14" height="14" viewBox="0 0 14 14" fill="none" stroke="#555" stroke-width="1.2"><circle cx="7" cy="7" r="6"/><path d="M1 7h12M7 1c2 2 2 10 0 12M7 1c-2 2-2 10 0 12"/></svg>
      All Locations
      <svg class="chev" width="10" height="6" viewBox="0 0 10 6" fill="none" stroke="#555" stroke-width="1.3"><path d="M1 1l4 4 4-4"/></svg>
    </span>
    <a class="find-btn">Find Jobs</a>
  </div>

  <h2 class="abs popular-title">Popular Searches</h2>
  <span class="abs tag" style="left:85px;top:519px">Agriculture</span>
  <span class="abs tag" style="left:230px;top:521px">Fisheries</span>
  <span class="abs tag" style="left:85px;top:571px">Constructions &amp; mining</span>
</section>

<!-- Search by Category -->
<h2 class="abs section-title cat-title">Search by Category</h2>
<p class="abs cat-sub">Search your career opportunity with our categories</p>

<div class="abs cat-card active" style="left:85px;top:928px">
  <div class="cat-icon">
    <svg width="44" height="44" viewBox="0 0 44 44" fill="none" stroke="#fff" stroke-width="1.8"><circle cx="14" cy="9" r="4"/><path d="M14 13v14l-6 10M14 27l6 10M8 19h12M30 40V18M30 24c-4 0-6-3-6-6 4 0 6 3 6 6zM30 28c4 0 6-3 6-6-4 0-6 3-6 6zM4 40h36"/></svg>
  </div>
  <div class="cat-text"><h3>Agriculture</h3><p>1 open position</p></div>
</div>
<div class="abs cat-card" style="left:612px;top:928px">
  <div class="cat-icon">
    <svg width="44" height="44" viewBox="0 0 44 44" fill="none" stroke="#222" stroke-width="1.8"><path d="M22 4v6M22 10c-6 6-6 16 0 22 6-6 6-16 0-22zM14 38l8-6 8 6M20 20h4"/></svg>
  </div>
  <div class="cat-text"><h3>Fisheries</h3><p>1 open position</p></div>
</div>
<div class="abs cat-card" style="left:85px;top:1045px">
  <div class="cat-icon">
    <svg width="44" height="44" viewBox="0 0 44 44" fill="none" stroke="#222" stroke-width="1.8"><path d="M6 40h32M10 40V14h18v26M6 8h30M30 8v10M14 20h4M20 20h4M14 27h4M20 27h4M14 34h4M20 34h4"/></svg>
  </div>
  <div class="cat-text"><h3>Constructions</h3><p>1 open position</p></div>
</div>
<div class="abs cat-card" style="left:612px;top:1045px">
  <div class="cat-icon">
    <svg width="44" height="44" viewBox="0 0 44 44" fill="none" stroke="#222" stroke-width="1.8"><path d="M8 10c8-6 18-6 26 2M21 8l-12 26M6 40l10-10 8 4 8-10 6 16z"/></svg>
  </div>
  <div class="cat-text"><h3>Mining</h3><p>1 open position</p></div>
</div>
<a class="abs all-cat">All Category ›</a>

<!-- Featured Job-seeker Portal -->
<section class="abs featured"></section>
<h2 class="abs section-title feat-title">Featured Job-seeker Portal</h2>
<p class="abs feat-sub">Search your career opportunity through 12,800 jobs</p>

<article class="abs job-card" style="left:85px;top:1514px">
  <div class="abs chip"><span class="chip-icon"><svg width="18" height="18" viewBox="0 0 18 18" fill="none" stroke="#7a2a55" stroke-width="1.4"><path d="M3 16h12M9 16V6M9 9c-2 0-3-1-3-3 2 0 3 1 3 3zM9 11c2 0 3-1 3-3-2 0-3 1-3 3z"/></svg></span>Agriculture</div>
  <h3>Agriculture Dept.</h3>
  <div class="abs job-meta"><svg width="20" height="20" viewBox="0 0 14 14" fill="none" stroke="#444" stroke-width="1"><circle cx="7" cy="7" r="6"/><path d="M1 7h12M7 1c2 2 2 10 0 12M7 1c-2 2-2 10 0 12"/></svg><b>Papua New Guinea</b>Full Time</div>
  <p class="abs job-date">June 8, 2022 by<br><b>Korvani Staffing</b></p>
  <div class="abs job-thumb" role="img" aria-label="Employer thumbnail"></div>
</article>
<article class="abs job-card" style="left:436px;top:1514px">
  <div class="abs chip"><span class="chip-icon"><svg width="18" height="18" viewBox="0 0 18 18" fill="none" stroke="#7a2a55" stroke-width="1.4"><path d="M9 2v3M9 5c-3 3-3 8 0 11 3-3 3-8 0-11z"/></svg></span>Fisheries</div>
  <h3>Fisheries Dept.</h3>
  <div class="abs job-meta"><svg width="20" height="20" viewBox="0 0 14 14" fill="none" stroke="#444" stroke-width="1"><circle cx="7" cy="7" r="6"/><path d="M1 7h12M7 1c2 2 2 10 0 12M7 1c-2 2-2 10 0 12"/></svg><b>Australia</b>Internship</div>
  <p class="abs job-date">June 8, 2022 by<br><b>Korvani Staffing</b></p>
  <div class="abs job-thumb" role="img" aria-label="Employer thumbnail"></div>
</article>
<article class="abs job-card" style="left:788px;top:1514px">
  <div class="abs chip"><span class="chip-icon"><svg width="18" height="18" viewBox="0 0 18 18" fill="none" stroke="#7a2a55" stroke-width="1.4"><path d="M3 16h12M5 16V7h7v9M3 3h12M13 3v4"/></svg></span>Construction</div>
  <h3>Constructions &amp; mining</h3>
  <div class="abs job-meta"><svg width="20" height="20" viewBox="0 0 14 14" fill="none" stroke="#444" stroke-width="1"><circle cx="7" cy="7" r="6"/><path d="M1 7h12M7 1c2 2 2 10 0 12M7 1c-2 2-2 10 0 12"/></svg><b>Papua New Guinea</b>Part Time</div>
  <p class="abs job-date">June 8, 2022 by<br><b>Korvani Staffing</b></p>
  <div class="abs job-thumb" role="img" aria-label="Employer thumbnail"></div>
</article>

<article class="abs job-card" style="left:85px;top:1864px">
  <div class="abs chip"><span class="chip-icon"><svg width="18" height="18" viewBox="0 0 18 18" fill="none" stroke="#7a2a55" stroke-width="1.4"><path d="M3 16h12M5 16V7h7v9M3 3h12M13 3v4"/></svg></span>Construction</div>
  <h3>Constructions &amp; mining</h3>
  <div class="abs job-meta"><svg width="20" height="20" viewBox="0 0 14 14" fill="none" stroke="#444" stroke-width="1"><circle cx="7" cy="7" r="6"/><path d="M1 7h12M7 1c2 2 2 10 0 12M7 1c-2 2-2 10 0 12"/></svg><b>Papua New Guinea</b>Part Time</div>
  <p class="abs job-date">June 8, 2022 by<br><b>Korvani Staffing</b></p>
  <div class="abs job-thumb" role="img" aria-label="Employer thumbnail"></div>
</article>
<article class="abs job-card" style="left:436px;top:1864px">
  <div class="abs chip"><span class="chip-icon"><svg width="18" height="18" viewBox="0 0 18 18" fill="none" stroke="#7a2a55" stroke-width="1.4"><path d="M3 16h12M9 16V6M9 9c-2 0-3-1-3-3 2 0 3 1 3 3zM9 11c2 0 3-1 3-3-2 0-3 1-3 3z"/></svg></span>Agriculture</div>
  <h3>Agriculture Dept.</h3>
  <div class="abs job-meta"><svg width="20" height="20" viewBox="0 0 14 14" fill="none" stroke="#444" stroke-width="1"><circle cx="7" cy="7" r="6"/><path d="M1 7h12M7 1c2 2 2 10 0 12M7 1c-2 2-2 10 0 12"/></svg><b>Papua New Guinea</b>Full Time</div>
  <p class="abs job-date">June 8, 2022 by<br><b>Korvani Staffing</b></p>
  <div class="abs job-thumb" role="img" aria-label="Employer thumbnail"></div>
</article>
<article class="abs job-card" style="left:788px;top:1864px">
  <div class="abs chip"><span class="chip-icon"><svg width="18" height="18" viewBox="0 0 18 18" fill="none" stroke="#7a2a55" stroke-width="1.4"><path d="M9 2v3M9 5c-3 3-3 8 0 11 3-3 3-8 0-11z"/></svg></span>Fisheries</div>
  <h3>Fisheries Dept.</h3>
  <div class="abs job-meta"><svg width="20" height="20" viewBox="0 0 14 14" fill="none" stroke="#444" stroke-width="1"><circle cx="7" cy="7" r="6"/><path d="M1 7h12M7 1c2 2 2 10 0 12M7 1c-2 2-2 10 0 12"/></svg><b>Australia</b>Internship</div>
  <p class="abs job-date">June 8, 2022 by<br><b>Korvani Staffing</b></p>
  <div class="abs job-thumb" role="img" aria-label="Employer thumbnail"></div>
</article>

<a class="abs all-jobs">All Job Offer <span>›</span></a>

<!-- About -->
<div class="abs about-ring"></div>
<div class="abs about-photo" role="img" aria-label="Photo of a young man working on a laptop while seated on stacked timber logs"></div>
<h2 class="abs about-title">About Korvani Staffing</h2>
<div class="abs about-copy">
  <p>Lorem ipsum dolor sit amet, consectetur adipiscing elit. Praesent ut vehicula lectus. Integer suscipit erat in ligula molestie finibus. Proin ornare ipsum eget risus facilisis volutpat. Nunc tincidunt enim a sapien porttitor, non elementum metus placerat. Curabitur tristique metus at bibendum viverra. Cras hendrerit pellentesque nunc, a cursus leo aliquet sit ame</p>
  <p>Lorem ipsum dolor sit amet, consectetur adipiscing elit. Praesent ut vehicula lectus. Integer suscipit erat in ligula molestie finibus. Proin ornare ipsum eget risus facilisis volutpat.</p>
</div>
<a class="abs started">Get Started</a>

<!-- Contact -->
<section class="abs contact"></section>
<h2 class="abs section-title contact-title">Contact Us</h2>
<div class="abs contact-item" style="top:3314px">
  <span class="contact-dot"><svg width="18" height="18" viewBox="0 0 24 24" fill="var(--magenta)"><path d="M6.6 10.8a15 15 0 006.6 6.6l2.2-2.2a1 1 0 011-.25 11.4 11.4 0 003.6.57 1 1 0 011 1V20a1 1 0 01-1 1A17 17 0 013 4a1 1 0 011-1h3.5a1 1 0 011 1c0 1.25.2 2.45.57 3.57a1 1 0 01-.25 1z"/></svg></span>
  Call: 0400 518 274 (Australia)
</div>
<div class="abs contact-item" style="top:3379px">
  <span class="contact-dot"><svg width="18" height="18" viewBox="0 0 24 24" fill="var(--magenta)"><path d="M6.6 10.8a15 15 0 006.6 6.6l2.2-2.2a1 1 0 011-.25 11.4 11.4 0 003.6.57 1 1 0 011 1V20a1 1 0 01-1 1A17 17 0 013 4a1 1 0 011-1h3.5a1 1 0 011 1c0 1.25.2 2.45.57 3.57a1 1 0 01-.25 1z"/></svg></span>
  Call: 0400 518 274 (Papua New Guinea)
</div>
<div class="abs contact-item" style="top:3443px">
  <span class="contact-dot"><svg width="18" height="14" viewBox="0 0 18 14" fill="var(--magenta)"><path d="M0 0h18v14H0z"/><path d="M0 0l9 7 9-7" fill="none" stroke="#fff" stroke-width="1.5"/></svg></span>
  Email: hello@korvanistaffing.example
</div>
<div class="abs contact-item" style="top:3503px">
  <span class="contact-dot"><svg width="16" height="20" viewBox="0 0 16 20" fill="var(--magenta)"><path d="M8 0a8 8 0 00-8 8c0 6 8 12 8 12s8-6 8-12a8 8 0 00-8-8zm0 11a3 3 0 110-6 3 3 0 010 6z"/></svg></span>
  <span>Location: Papua New Guinea &amp;<br>Australia</span>
</div>

<form class="abs form-card">
  <h2>Get in Touch</h2>
  <div class="abs field" style="left:55px;top:127px"><label>First Name</label><span><i class="caret"></i></span></div>
  <div class="abs field" style="left:311px;top:127px"><label>Last Name</label><span>Jhon Doe</span></div>
  <div class="abs field" style="left:55px;top:213px"><label>Email</label><span>info@example.com</span></div>
  <div class="abs field" style="left:311px;top:213px"><label>Phone</label><span>+01 234 567 89</span></div>
  <div class="abs field wide" style="left:55px;top:298px"><label>Your Message</label><span>Your message here</span></div>
  <a class="abs submit">Submit</a>
</form>

<!-- Footer -->
<div class="abs foot-logo logo"><span>Korvani</span><span>Staffing</span></div>
<p class="abs foot-about">Praesent eu magna ultricies, aliquet eros a, dignissim ligula. Fusce bibendum sed dui sed ultrices. Phasellus sapien tortor, accumsan quis odio sit amet, aliquet auctor mi. Aliquam vulputate tortor ex, laoreet sodales libero tempus quis. Integer convallis porttitor venenatis.</p>

<div class="abs foot-col" style="left:498px;top:3804px">
  <h4>Quick Links</h4><div class="bar"></div>
  <ul><li>Home</li><li>About Us</li><li>Services</li><li>Job Seeker portal</li><li>Training</li></ul>
</div>
<div class="abs foot-col" style="left:680px;top:3802px">
  <h4>Other Links</h4><div class="bar"></div>
  <ul><li>Our Team</li><li>Gallery</li><li>FAQ</li><li>Reviews</li><li>Contact</li></ul>
</div>
<div class="abs foot-col foot-contact" style="left:864px;top:3802px">
  <h4>Contact</h4><div class="bar"></div>
  <ul>
    <li><svg width="14" height="17" viewBox="0 0 16 20" fill="var(--magenta)"><path d="M8 0a8 8 0 00-8 8c0 6 8 12 8 12s8-6 8-12a8 8 0 00-8-8zm0 11a3 3 0 110-6 3 3 0 010 6z"/></svg><span><b>Location:</b> Papua New Guinea &amp;<br>Australia</span></li>
    <li style="margin-top:10px"><svg width="14" height="14" viewBox="0 0 24 24" fill="var(--magenta)"><path d="M6.6 10.8a15 15 0 006.6 6.6l2.2-2.2a1 1 0 011-.25 11.4 11.4 0 003.6.57 1 1 0 011 1V20a1 1 0 01-1 1A17 17 0 013 4a1 1 0 011-1h3.5a1 1 0 011 1c0 1.25.2 2.45.57 3.57a1 1 0 01-.25 1z"/></svg><span><b>Call:</b> 0400 518 274 (Papua New<br>Guinea)</span></li>
    <li><svg width="14" height="14" viewBox="0 0 24 24" fill="var(--magenta)"><path d="M6.6 10.8a15 15 0 006.6 6.6l2.2-2.2a1 1 0 011-.25 11.4 11.4 0 003.6.57 1 1 0 011 1V20a1 1 0 01-1 1A17 17 0 013 4a1 1 0 011-1h3.5a1 1 0 011 1c0 1.25.2 2.45.57 3.57a1 1 0 01-.25 1z"/></svg><span><b>Call:</b> 0400 518 274 (Australia)</span></li>
    <li><svg width="15" height="12" viewBox="0 0 18 14" fill="var(--magenta)"><path d="M0 0h18v14H0z"/><path d="M0 0l9 7 9-7" fill="none" stroke="#fff" stroke-width="1.5"/></svg><span><b>Email:</b> hello@korvanistaffing.example</span></li>
  </ul>
</div>

<div class="abs foot-rule" style="left:86px;width:372px"></div>
<div class="abs foot-rule" style="left:742px;width:372px"></div>
<p class="abs copyright">Copyright © 2022. All right reserved.</p>

</body>
</html>
```